Brackenmoor Heating Supplies Ltd Needs a 2 sided A5 Flyer Design

We need a flyer design for our company to promote Air and ground Source Heat Pumps in the Devon and Cornwall region of the UK.

Our Government has launched the RHI (renewable heat incentive) a 7 year quarterly payment to offset the cost of installation..
Homeowners currently using OIL or LPG gas for there heating and hot water will save up to 50% on there energy bill by swapping to a heat pump,
Currently education is needed to the potential end user on the benefits of heat pumps,
This flyer will be part of an initial start point to get the homeowner to book a free survey to discuss there options, We are a renewable energy company with great local knowledge, and a wealth of experience ......

KEY points SAVINGS OF UP TO 50% on OIL or LPG heating and hot water systems

RHI PAYMENTS FROM GOVERNMENT FOR 7 years

HONEST IMPARTIAL ADVICE ON SOLUTIONS

FREE SURVEYS ON ALL RENEWABLE SOLUTIONS AND COSTINGS. website www.brackenmoorheat.co.uk have included some potential wording

LOGOS FROM SUPPLIERS

We think side one should be high impact on high oil and LPG gas costs, harm to environment and potential 50% savings with a heat pump. Side 2 to be RHI 7 year quarterly payment and a little about our company offering expertise and free impartial advice and survey

general theme a "striking call to action"

Target Market(s)

Target market is 40 to 60 year old home owners that are off gas grid and use oil or LPG for heating and hot water

Industry/Entity Type

Environment

Font styles to use
Serif
Sans Serif

Colors
33a6d7
f04a50
00a88f
fbed22

Requirements
Must have
• savings 50% on oil or LPG energy costs for heating and hot water

RHI (renewable heat incentive) government backed payments to offset cost of instalation

7 year payments averaging £1000 a year

FREE impartial advice and surveys

```html
<!DOCTYPE html>
<html lang="en">
<head>
<meta charset="utf-8">
<title>Brackenmoor Heating Supplies – Heat Pump Flyer</title>
<link rel="stylesheet" href="https://fonts.googleapis.com/css2?family=Oswald:wght@300;400;500;600&display=swap">
<style>
  :root{
    --page:#0b0b0b;
    --white:#ffffff;
    --green:#6aa527;
    --green-light:#9ccd3c;
    --green-dark:#3f6f14;
    --green-deep:#2f5a0c;
    --text-green:#5e9a1d;
    --red:#e3262a;
    --grey-dark:#3a3a3a;
    --photo-dark:#2b2b2b;
  }
  *{margin:0;padding:0;box-sizing:border-box}
  html,body{width:895px;height:1200px;overflow:hidden;background:var(--page)}
  body{font-family:'Oswald',Arial,sans-serif;position:relative}
  .flyer{position:absolute;left:31px;top:0;width:833px;height:1174px;background:var(--white);overflow:hidden}
  .hero-photo{position:absolute;left:0;top:0;width:833px;height:440px;
    background:linear-gradient(160deg,#f0f0f0 0%,#8c8c8c 35%,var(--photo-dark) 60%,#bdbdbd 85%,#7a7a7a 100%)}
  .swoosh{position:absolute;left:0;top:0;width:833px;height:1174px}
  .headline{position:absolute;left:60px;top:76px;color:var(--white);font-weight:600;font-size:62px;line-height:78px;letter-spacing:.5px}
  .badge-photo{position:absolute}
  .title-small{position:absolute;right:394px;top:462px;color:var(--green-light);font-size:32px;line-height:40px;font-weight:400}
  .title-large{position:absolute;right:394px;top:508px;color:var(--white);font-size:52px;line-height:64px;font-weight:400;letter-spacing:.3px;white-space:nowrap}
  .savings{position:absolute;left:572px;top:434px;width:206px;height:206px;border-radius:50%;
    background:var(--green-dark);border:6px solid var(--green-light);color:var(--white);text-align:center}
  .savings .lead{display:block;margin-top:20px;font-size:25px;line-height:32px;font-weight:400;color:#e7f3d2}
  .savings .figure{display:block;font-size:72px;line-height:76px;font-weight:500}
  .savings .figure small{font-size:32px}
  .savings .note{display:block;font-size:13px;line-height:16px;font-weight:400;padding:0 34px}
  .product-photo{position:absolute;left:40px;top:640px;width:400px;height:315px;
    background:linear-gradient(180deg,#f4f4f4,#cfcfcf)}
  .benefits{position:absolute;right:39px;top:760px;list-style:none;text-align:right;color:var(--text-green);font-size:18px;font-weight:300;line-height:24px}
  .benefits li{margin-bottom:20px}
  .partners{position:absolute;left:32px;top:1036px;height:54px;width:400px}
  .partners .caption{position:absolute;left:0;top:0;font-size:7px;color:#666;letter-spacing:.3px}
  .partner{position:absolute}
  .brand{position:absolute;right:30px;top:962px;display:flex;align-items:flex-end;gap:12px;color:var(--grey-dark);font-weight:400}
  .brand-mark{width:42px;height:42px;background:var(--green);margin-bottom:62px}
  .brand-name{text-align:right;line-height:1.05}
  .brand-name .line1{display:block;font-size:38px}
  .brand-name .line2{display:block;font-size:22px}
  .footer-band{position:absolute;left:0;bottom:0;width:833px;height:60px;background:var(--green)}
  .web{position:absolute;right:36px;top:12px;color:var(--white);font-size:27px;font-weight:400;letter-spacing:.8px}
</style>
</head>
<body>
<main class="flyer">
  <div class="hero-photo" role="img" aria-label="Photograph of rows of used oil drums"></div>

  <svg class="swoosh" viewBox="0 0 833 1174" aria-hidden="true">
    <path d="M0,420 C250,360 560,250 833,140 L833,1174 L0,1174 Z" fill="var(--green-deep)"/>
    <path d="M0,400 C250,330 560,230 833,115 L833,170 C560,280 260,380 0,440 Z" fill="var(--green-light)"/>
    <path d="M0,440 C260,385 560,290 833,180 L833,460 C620,570 320,650 0,665 Z" fill="var(--green)"/>
    <path d="M0,665 C320,650 620,570 833,460 L833,1174 L0,1174 Z" fill="var(--white)"/>
  </svg>

  <h1 class="headline">NO TO OIL<br>NO TO LPG</h1>

  <svg class="badge-photo" style="left:387px;top:160px" width="196" height="196" viewBox="0 0 200 200" role="img" aria-label="Photograph of a spilling black oil drum">
    <circle cx="100" cy="100" r="92" fill="#4d4d4d" stroke="var(--green)" stroke-width="7"/>
    <line x1="52" y1="52" x2="148" y2="148" stroke="var(--red)" stroke-width="6"/>
    <line x1="148" y1="52" x2="52" y2="148" stroke="var(--red)" stroke-width="6"/>
  </svg>
  <svg class="badge-photo" style="left:600px;top:62px" width="200" height="200" viewBox="0 0 200 200" role="img" aria-label="Photograph of blue LPG gas bottles">
    <circle cx="100" cy="100" r="92" fill="#3f8fb8" stroke="var(--green)" stroke-width="7"/>
    <line x1="52" y1="52" x2="148" y2="148" stroke="var(--red)" stroke-width="6"/>
    <line x1="148" y1="52" x2="52" y2="148" stroke="var(--red)" stroke-width="6"/>
  </svg>

  <p class="title-small">AIR AND GROUND</p>
  <h2 class="title-large">SOURCE HEAT PUMPS</h2>

  <div class="savings">
    <span class="lead">save up to</span>
    <span class="figure">50<small>%</small></span>
    <span class="note">on there energy bill by swapping to a heat pump</span>
  </div>

  <div class="product-photo" role="img" aria-label="Photograph of an outdoor air source heat pump unit"></div>

  <ul class="benefits">
    <li>RHI PAYMENTS FROM GOVERNMENT FOR 7 years</li>
    <li>HONEST IMPARTIAL ADVICE ON SOLUTIONS</li>
    <li>FREE SURVEYS ON ALL RENEWABLE SOLUTIONS<br>AND COSTINGS</li>
  </ul>

  <div class="partners">
    <span class="caption">APPROVED INSTALLER</span>
    <svg class="partner" style="left:0;top:10px" width="40" height="40" aria-hidden="true"><circle cx="20" cy="20" r="18" fill="#b9c7d6"/></svg>
    <svg class="partner" style="left:58px;top:12px" width="32" height="38" aria-hidden="true"><rect x="2" y="2" width="28" height="34" fill="#9aa3b5"/></svg>
    <svg class="partner" style="left:118px;top:0" width="108" height="52" aria-hidden="true"><rect width="108" height="52" fill="var(--red)"/></svg>
    <svg class="partner" style="left:252px;top:6px" width="130" height="42" aria-hidden="true"><rect width="130" height="42" rx="6" fill="#cfe3f3"/></svg>
  </div>

  <div class="brand">
    <span class="brand-mark" aria-hidden="true"></span>
    <p class="brand-name"><span class="line1">Brackenmoor</span><span class="line2">Heating Supplies Ltd</span></p>
  </div>

  <footer class="footer-band">
    <p class="web">WWW.BRACKENMOORHEAT.CO.UK</p>
  </footer>
</main>
</body>
</html>
```